Brochure to promote unique premium vehicle brokerage and detailing service

We are a new business offering a unique way of selling your car privately. We yield our customers higher than trade in and consignment returns on second hand vehicles, positioning each vehicle as best in the market to achieve the optimum outcome. We manage the whole process from start to finish so customers don't have to do any of the administration, negotiating or physical work attached to selling a car.

The problem is no one knows this service exists. We want people to know we are new, honest and worthwhile - they will end up with more in their pocket using our help. We also need to appeal to the 'right' customers. We are looking to attract customers selling cars worth greater than $AUD 50,000 second hand. In all our material we try to convey a luxury, premium feel. We have a website and logo for which we provided similar brief.

There is another side to our business, which is mobile car detailing and paint protection. This is a competitive market and again, we target luxury car owners. Our services are far superior to any bricks and mortar car wash or detailing facility and the average Velmora driver is probably not going to see value in what we offer.

I am not sure whether this brief is for a brochure or a flyer, it is probably something in between? I am envisioning probably 1 A4 sheet folded to create 3 columns, potentially setting out the 2 sides of the business 1 on each side? I am very open to all suggestions/advice. It may make more sense to split the 2 entirely.

We don't want detailed pricing set out as we want to brochure to be valid for a long time. I would prefer a "starting at" for the detailing and paint protection and no specific price on the sales side of things as it is too complex to explain in a brochure.

We have a website which we did our own copywriting for so you could use some of that text. Please let me know in your response if copywriting represents a challenge. Our previous freelancer withdrew because she was unable to write. I am specifically looking for someone who can prepare decent marketing text.

We are Sydney based and available for phone, face to face or email communication. Our website is www.crestmoorautocare.com.au. I have attached a couple of logo files but I do have other formats of the images.

Target Market(s)

These customers are inexperienced or uncomfortable negotiators. They have potentially be putting off buying a vehicle for fear of the process, or are unaware of their negotiating power at a vehicle dealer.

Industry/Entity Type

Marketing

Font styles to use
Other font styles liked:
• Arial is close. Please check our website

Requirements
Must have
• I would like the designer to write the content. Most of this can come from our website. I wrote all of it myself and have it in word format if that is easier to work with.
Nice to have
• We operate 2 service streams - the vehicle brokerage service and a premium detailing service. My biggest priority is targeting vehicle sales/brokerage customers currently. Therefore I am open to dedicating all the energy to that purpose and separately scoping the detailing services if appropriate.
• However, if the flyer could be multi purpose and address both services, maybe one on each side, that may serve me better. The target market for detailing services is vehicle owners of luxury vehicles who are discerning in their preference for perfect presentation of their vehicle, yet do not have the time or ability to achieve this independently.
Should not have
• cartoons,caricatures, gimmicky items that cheapen the feel.

```html
<!DOCTYPE html>
<html lang="en">
<head>
<meta charset="utf-8">
<title>Crestmoor Auto Care – Brochure</title>
<link rel="stylesheet" href="https://fonts.googleapis.com/css2?family=Anton&family=Lato:wght@400;700&display=swap">
<style>
  :root{
    --blue-deep:#0f3f94;
    --blue:#1a5fc0;
    --blue-bright:#2b8fe0;
    --blue-sky:#5cb6ef;
    --ink:#3a3a3a;
    --grey:#666;
    --paper:#ffffff;
    --stage:#e8ebef;
  }
  *{box-sizing:border-box;margin:0;padding:0}
  html,body{width:1200px;height:626px;overflow:hidden;background:var(--stage);font-family:"Lato",Arial,sans-serif}
  .canvas{position:relative;width:1200px;height:626px}

  /* ---------- spread ---------- */
  .spread{position:absolute;left:12px;top:52px;width:706px;height:528px;overflow:hidden;box-shadow:0 4px 14px rgba(0,0,0,.25);background:var(--paper)}
  .spread svg{position:absolute;inset:0}
  .about-tab{position:absolute;left:0;top:68px;width:96px;height:30px;background:var(--blue-bright);border-radius:0 8px 8px 0;color:#fff;font-weight:700;font-size:17px;line-height:30px;padding-left:14px}
  .about-copy{position:absolute;left:15px;top:114px;width:215px;color:#fff;font-weight:700;font-size:12.4px;line-height:14.6px}
  .audience{position:absolute;left:15px;top:402px;width:240px;color:var(--ink);font-size:17px;line-height:20.5px}
  .audience em{font-style:normal;color:var(--blue-bright)}
  .brand-block{position:absolute;left:272px;top:402px;width:180px;text-align:center}
  .brand-mark{display:block;width:22px;height:22px;margin:0 auto 8px;border-radius:50%;background:var(--blue)}
  .brand-name{color:var(--blue);font-size:14px;font-weight:400;letter-spacing:.3px}
  .phone{margin-top:6px;color:var(--blue);font-size:17px;display:flex;align-items:center;justify-content:center;gap:5px}
  .phone svg{position:static;width:13px;height:13px}
  .welcome{position:absolute;left:478px;top:424px;width:220px;text-align:center}
  .welcome h2{font-family:"Anton",Impact,sans-serif;font-weight:400;color:var(--blue);font-size:16px;line-height:19px;letter-spacing:.2px}
  .welcome p{margin-top:4px;color:var(--grey);font-size:6.6px;line-height:9px}

  /* ---------- flyer cover ---------- */
  .flyer{position:absolute;left:790px;top:30px;width:330px;height:566px;background:var(--paper);overflow:hidden;box-shadow:0 4px 14px rgba(0,0,0,.25)}
  .flyer svg{position:absolute;inset:0}
  .flyer-brand{position:absolute;top:20px;left:0;right:0;text-align:center}
  .flyer-brand .brand-mark{width:26px;height:26px;margin-bottom:8px}
  .flyer-brand .brand-name{font-size:17px}
  .flyer-welcome{position:absolute;left:22px;right:22px;top:368px;text-align:center}
  .flyer-welcome h2{font-family:"Anton",Impact,sans-serif;font-weight:400;color:var(--blue);font-size:27px;line-height:31px}
  .flyer-welcome p{margin-top:8px;color:var(--grey);font-size:12px;line-height:15px}
</style>
</head>
<body>
<main class="canvas">

  <section class="spread">
    <svg width="706" height="528" viewBox="0 0 706 528" aria-hidden="false">
      <defs>
        <linearGradient id="panelBlue" x1="0" y1="0" x2="1" y2="1">
          <stop offset="0" stop-color="#2a7fd8"/>
          <stop offset="1" stop-color="#0f3f94"/>
        </linearGradient>
        <linearGradient id="lotScene" x1="0" y1="0" x2="0" y2="1">
          <stop offset="0" stop-color="#cfe0f2"/>
          <stop offset=".25" stop-color="#e8eef4"/>
          <stop offset=".33" stop-color="#8c9a5a"/>
          <stop offset=".45" stop-color="#9aa59a"/>
          <stop offset=".7" stop-color="#6d7378"/>
          <stop offset="1" stop-color="#4f5458"/>
        </linearGradient>
      </defs>
      <rect class="panel" width="706" height="372" fill="url(#panelBlue)"/>
      <path d="M130 0 C150 120 200 250 300 330 C380 370 520 350 706 260 V372 H0 V0Z" fill="#1c58b8" opacity=".6"/>
      <path d="M230 372 C330 360 520 340 706 250 V300 C560 360 400 372 300 372Z" fill="#5cb6ef" opacity=".8"/>
      <path role="img" aria-label="Photo of a row of silver sedans parked on a lot beneath trees and a cloudy sky"
            d="M73 0 H706 V240 C620 320 520 352 420 350 C330 348 260 336 212 318 C150 270 105 150 73 0Z"
            fill="url(#lotScene)"/>
      <path d="M73 0 C105 150 150 270 212 318" fill="none" stroke="#5cb6ef" stroke-width="3"/>
      <rect y="372" width="706" height="156" fill="#fff"/>
      <rect y="362" width="706" height="5" fill="var(--blue-bright)"/>
      <rect y="500" width="706" height="6" fill="var(--blue-bright)"/>
      <rect y="510" width="706" height="18" fill="var(--blue)"/>
    </svg>

    <div class="about-tab">About US</div>
    <p class="about-copy">We are a new business offering a unique way of selling your car privately. We yield our customers higher than trade in and consignment returns on second hand vehicles, positioning each vehicle as best in the market to achieve the optimum outcome. We manage the whole process from start to finish so customers don't have to do any of the administration, negotiating or physical work attached to selling a car.</p>

    <p class="audience">We are looking to attract customers selling cars worth greater than <em>$AUD 50,000</em> second hand.</p>

    <div class="brand-block">
      <span class="brand-mark"></span>
      <div class="brand-name">Crestmoor Auto Care</div>
      <div class="phone">
        <svg viewBox="0 0 24 24"><rect x="1" y="1" width="22" height="22" rx="4" fill="var(--blue)"/><path d="M8 6l2 3-1.5 1.5c.8 1.8 2.2 3.2 4 4L14 13l3 2-1 2.5c-4.5-.5-8.5-4.5-9-9z" fill="#fff"/></svg>
        0400 555 017
      </div>
    </div>

    <div class="welcome">
      <h2>WELCOME TO CRESTMOOR<br>AUTO CARE</h2>
      <p>Cars are our passion and I guess you could label us obsessed with all things automotive. Whether you are selling, buying, maintaining or modifying we are sure we can help you.</p>
    </div>
  </section>

  <section class="flyer">
    <svg width="330" height="566" viewBox="0 0 330 566">
      <defs>
        <linearGradient id="flyerScene" x1="0" y1="0" x2="0" y2="1">
          <stop offset="0" stop-color="#8c9a5a"/>
          <stop offset=".3" stop-color="#9aa59a"/>
          <stop offset=".7" stop-color="#6d7378"/>
          <stop offset="1" stop-color="#4f5458"/>
        </linearGradient>
      </defs>
      <path role="img" aria-label="Photo of a row of silver sedans parked on a lot beside a grassy field"
            d="M0 90 H330 V270 C240 300 120 300 0 280Z" fill="url(#flyerScene)"/>
      <path d="M0 280 C120 300 240 300 330 270 V330 C220 345 110 340 0 320Z" fill="var(--blue-bright)"/>
      <path d="M0 300 C120 320 240 318 330 295 V350 H0Z" fill="var(--blue)"/>
      <rect y="350" width="330" height="216" fill="#fff"/>
      <rect y="520" width="330" height="6" fill="var(--blue-bright)"/>
      <rect y="532" width="330" height="34" fill="var(--blue)"/>
    </svg>
    <div class="flyer-brand">
      <span class="brand-mark"></span>
      <div class="brand-name">Crestmoor Auto Care</div>
    </div>
    <div class="flyer-welcome">
      <h2>WELCOME TO CRESTMOOR<br>AUTO CARE</h2>
      <p>Cars are our passion and I guess you could label us obsessed with all things automotive. Whether you are selling, buying, maintaining or modifying we are sure we can help you.</p>
    </div>
  </section>

</main>
</body>
</html>
```